Tiny Petal Product Label for Tear-Free Head-to-Toe Wash

Need a bottle label design for a new line of natural products targeting infants and children. Products are Pediatrician-developed and paraben-free, sulfate-free, fragrance-free, and cruelty-free. Design should be clean and have a high-end feel to it. Will need other product labels in Tiny Petal line designed as well in upcoming projects.

Target Market(s)

Newborn to young elementary age children and their parents

Industry/Entity Type

Cosmetics/Beauty

Font styles to use
Other font styles liked:
• Brand fonts are Jost and Sonorous

Colors

Designer to choose colors to be used in the design.

Requirements
Must have
• Tiny Petal logo, Pediatrician Developed logo, and a clean high-end feel to it. The label must fit the specialty bottle we will be using (label measurements and diagram will be provided) for the front and back of bottle only (NOT the side labels). It must include our list of ingredients (will provide once designer selected).
Nice to have
• Should stand out on the shelf of other baby products due to it's clean simplicity and high-end feel
Should not have
• too much of a "kiddie" feel to it (targeting the parents not the kids)

```html
<!DOCTYPE html>
<html lang="en">
<head>
<meta charset="utf-8">
<title>Tiny Petal – Tear-Free Head-to-Toe Wash Label</title>
<link href="https://fonts.googleapis.com/css2?family=Jost:wght@500;600&family=Arimo:ital,wght@0,400;0,700;1,400;1,700&display=swap" rel="stylesheet">
<style>
  :root {
    --page: #ffffff;
    --label-cream: #faf8f4;
    --gold: #98722f;
    --gold-soft: #efe8dc;
    --ink: #222222;
    --white: #ffffff;
  }
  * { margin: 0; padding: 0; box-sizing: border-box; }
  html, body { width: 1200px; height: 1200px; overflow: hidden; background: var(--page); }
  .sheet { position: relative; width: 1200px; height: 1200px; }

  .label {
    position: absolute; top: 270px; width: 460px; height: 660px;
    background: var(--label-cream);
    border-radius: 120px 120px 0 0 / 70px 70px 0 0;
    overflow: hidden;
    font-family: "Arimo", Arial, sans-serif;
    box-shadow: 0 0 0 1px #eeeae3;
  }
  .label--front { left: 100px; }
  .label--back { left: 640px; }

  .front__swoosh, .front__base { position: absolute; left: 0; top: 0; }

  .brand-mark {
    position: absolute; left: 165px; top: 52px; width: 130px; height: 130px;
    border-radius: 50%; border: 4px solid var(--gold);
  }
  .brand-name {
    position: absolute; left: 0; width: 100%; top: 196px; text-align: center;
    font-family: "Jost", sans-serif; font-weight: 600; font-size: 44px;
    color: var(--ink); letter-spacing: 1px;
  }
  .brand-tagline {
    position: absolute; left: 0; width: 100%; top: 254px; text-align: center;
    font-family: "Jost", sans-serif; font-weight: 600; font-size: 11px;
    letter-spacing: 2.2px; color: var(--gold);
  }
  .product-title {
    position: absolute; left: 0; width: 100%; top: 304px; text-align: center;
    font-weight: 700; font-size: 27px; line-height: 33px; color: var(--ink);
  }
  .product-subtitle {
    position: absolute; left: 0; width: 100%; top: 375px; text-align: center;
    font-style: italic; font-size: 16px; color: var(--gold);
  }
  .claim-badge {
    position: absolute; width: 58px; height: 58px; border-radius: 50%;
    border: 1.5px solid var(--gold);
  }
  .net-weight {
    position: absolute; left: 0; width: 100%; top: 616px; text-align: center;
    font-weight: 700; font-size: 21px; color: var(--white);
  }

  .back__mark {
    position: absolute; left: 208px; top: 36px; width: 46px; height: 46px;
    border-radius: 50%; border: 2px solid var(--gold);
  }
  .back__copy {
    position: absolute; left: 58px; width: 344px;
    font-size: 18px; line-height: 23.5px; letter-spacing: -0.1px; color: var(--ink);
    text-align: justify; text-align-last: center;
  }
  .back__intro { top: 96px; }
  .back__directions { top: 262px; }
  .back__ingredients { top: 403px; }
  .back__heading {
    position: absolute; left: 0; width: 100%; text-align: center;
    font-weight: 700; font-style: italic; font-size: 22px; color: var(--gold);
  }
  .back__heading--directions { top: 234px; }
  .back__heading--ingredients { top: 375px; }
  .maker {
    position: absolute; left: 58px; top: 546px;
    font-size: 18px; line-height: 23.5px; color: var(--ink);
  }
  .maker__title { font-weight: 700; font-style: italic; color: var(--gold); }
  .pediatrician-badge {
    position: absolute; left: 336px; top: 536px; width: 78px; height: 78px;
    border-radius: 50%; border: 1.5px solid var(--gold);
  }
</style>
</head>
<body>
<main class="sheet">

  <section class="label label--front" aria-label="Front label">
    <svg class="front__swoosh" width="460" height="660" viewBox="0 0 460 660" aria-hidden="true">
      <path d="M55 300 C160 230 330 250 460 360" fill="none" stroke="var(--gold-soft)" stroke-width="16" stroke-linecap="round"/>
      <path d="M0 410 C80 380 150 370 220 372" fill="none" stroke="var(--gold-soft)" stroke-width="12" stroke-linecap="round"/>
    </svg>
    <svg class="front__base" width="460" height="660" viewBox="0 0 460 660" aria-hidden="true">
      <path d="M0 415 C10 520 90 560 180 548 C290 535 380 470 460 450 L460 660 L0 660 Z" fill="var(--gold)"/>
    </svg>

    <div class="brand-mark" aria-hidden="true"></div>
    <h1 class="brand-name">Tiny Petal</h1>
    <p class="brand-tagline">GENTLY, FROM THE VERY FIRST DAY</p>
    <h2 class="product-title">Tear-Free<br>Head-to-Toe Wash</h2>
    <p class="product-subtitle">Naturally formulated for delicate skin</p>

    <div class="claim-badge" style="left:54px;top:460px" aria-label="Paraben free"></div>
    <div class="claim-badge" style="left:133px;top:480px" aria-label="Sulfate free"></div>
    <div class="claim-badge" style="left:210px;top:458px" aria-label="Fragrance free"></div>
    <div class="claim-badge" style="left:286px;top:422px" aria-label="Cruelty free"></div>

    <p class="net-weight">Net wt: 73 mL/2,43 fl.oz</p>
  </section>

  <section class="label label--back" aria-label="Back label">
    <div class="back__mark" aria-hidden="true"></div>
    <p class="back__copy back__intro">A gentle, all-in-one cleanser made with natural ingredients to protect and nourish baby’s delicate hair and skin. Pediatrician-developed and suitable for daily use from newborn onwards.</p>

    <h3 class="back__heading back__heading--directions">Directions:</h3>
    <p class="back__copy back__directions">Dispense a small amount into hands or washcloth. Gently massage into wet hair and skin. Rinse thoroughly. Avoid contact with eyes.</p>

    <h3 class="back__heading back__heading--ingredients">Ingredients:</h3>
    <p class="back__copy back__ingredients">Aqua, Glycerin, Decyl Glucoside, Sodium Lauroyl Lactylate, Coco-Glucoside, Glyceryl Oleate, Xanthan Gum, Sodium Benzoate, Citric Acid. (Full list to be finalized.)</p>

    <p class="maker">
      <span class="maker__title">Manufactured for</span><br>
      Tiny Petal Co.<br>
      tinypetalcare.com/Made in USA
    </p>
    <div class="pediatrician-badge" aria-label="Pediatrician developed"></div>
  </section>

</main>
</body>
</html>
```